graphics for landing page on website

need art work for a game called march of ravens.
players will have a choice of playing the following characters
-gangster, farmer, banker, salesman, cop, assassin , mercenary

This project will go on the front of the website.

goal of the game is to create a strong cartel to battle other cartels.

this can be text only or can incorporate some of the characters. looking for modern design. game will taget male players 18-40 years old

18-40 males

Farmer

```html
<!DOCTYPE html>
<html lang="en">
<head>
<meta charset="utf-8">
<title>March of Ravens</title>
<link rel="stylesheet" href="https://fonts.googleapis.com/css2?family=Anton&display=swap">
<style>
  :root {
    --teal: #2fbcbc;
    --teal-light: #4fc9c6;
    --teal-deep: #1c9fa3;
    --red: #c00808;
    --red-deep: #7a0003;
    --red-mid: #a10405;
    --ink: #0a0a0a;
  }
  html, body {
    margin: 0;
    padding: 0;
    width: 1200px;
    height: 900px;
    overflow: hidden;
    background: var(--red);
  }
  .hero {
    position: relative;
    width: 1200px;
    height: 900px;
    overflow: hidden;
    background:
      radial-gradient(ellipse 260px 200px at 1180px 880px, var(--teal-light) 0%, rgba(79,201,198,0.6) 45%, rgba(79,201,198,0) 100%),
      radial-gradient(ellipse 520px 420px at 1050px 80px, var(--red-deep) 0%, rgba(122,0,3,0) 100%),
      radial-gradient(ellipse 420px 500px at 150px 300px, var(--teal-light) 0%, rgba(79,201,198,0) 100%),
      radial-gradient(ellipse 300px 380px at 80px 780px, var(--teal-deep) 0%, rgba(28,159,163,0) 100%),
      linear-gradient(90deg, var(--teal) 0%, var(--teal) 33%, #6a8a8e 40%, var(--red-mid) 47%, var(--red) 60%, var(--red) 100%);
  }
  .hero__title {
    position: absolute;
    left: 0;
    top: 0;
    width: 1200px;
    height: 900px;
  }
  .hero__title text {
    font-family: "Anton", "Impact", sans-serif;
    font-size: 172px;
    letter-spacing: 4px;
  }
</style>
</head>
<body>
  <main class="hero">
    <svg class="hero__title" viewBox="0 0 1200 900" aria-labelledby="game-title">
      <defs>
        <linearGradient id="title-fill" gradientUnits="userSpaceOnUse" x1="0" y1="0" x2="1200" y2="0">
          <stop offset="0" stop-color="#35b4b4"/>
          <stop offset="0.32" stop-color="#3aa9ab"/>
          <stop offset="0.42" stop-color="#6d6a70"/>
          <stop offset="0.5" stop-color="#b01316"/>
          <stop offset="1" stop-color="#c8090b"/>
        </linearGradient>
        <filter id="title-shadow" x="-5%" y="-20%" width="110%" height="140%">
          <feDropShadow dx="0" dy="3" stdDeviation="4" flood-color="#000" flood-opacity="0.7"/>
        </filter>
      </defs>
      <text id="game-title" x="600" y="516" text-anchor="middle"
            textLength="1084" lengthAdjust="spacingAndGlyphs"
            fill="url(#title-fill)" stroke="var(--ink)" stroke-width="4"
            paint-order="stroke" filter="url(#title-shadow)">MARCH OF RAVENS</text>
    </svg>
  </main>
</body>
</html>
```